CORAL REFRIGERATION Business Card design

We are looking for a business card design front and back. We would like our logo only on the front with all other details on the rear.
Rear should include name, email address and two phone numbers. Similar to the attachment.
Smart and bright.
Looking for a matt finish on all of the card but the logo to be gloss and slightly proud.

Contact Information for Business Card

Name - Gavin Pellow
Director
Phone - 0893172648
0417258391
email - gavin@coralrefrigeration.com.au
website - coralrefrigeration.com.au

Font styles to use
Serif

Requirements
Must have
• Colours from our logo. icons for phone, email etc.

```html
<!DOCTYPE html>
<html lang="en">
<head>
<meta charset="utf-8">
<title>Coral Refrigeration – Business Card</title>
<link rel="stylesheet" href="https://fonts.googleapis.com/css2?family=Open+Sans:wght@400;600&family=Ubuntu:wght@700&display=swap">
<style>
  :root {
    --backdrop: #141414;
    --card: #1f1f1f;
    --card-edge: #2a2a2a;
    --lime: #9ef55f;
    --silver: #d2d2d2;
    --ink: #ececec;
    --rule: #2e2e2e;
  }
  * { box-sizing: border-box; margin: 0; padding: 0; }
  html, body {
    width: 1200px; height: 900px; overflow: hidden;
    background: var(--backdrop);
    font-family: "Open Sans", Arial, sans-serif;
  }
  .stage { position: relative; width: 1200px; height: 900px; }
  .card {
    position: absolute;
    width: 560px; height: 340px;
    background: var(--card);
    border: 1px solid var(--card-edge);
    border-radius: 26px;
    box-shadow: 0 18px 40px rgba(0,0,0,.55);
  }
  .card--front { left: 90px; top: 80px; display: flex; align-items: center; justify-content: center; }
  .card--back { left: 550px; top: 470px; }

  .wordmark {
    font-family: "Ubuntu", Arial, sans-serif;
    font-weight: 700;
    text-align: center;
    line-height: 1.05;
    letter-spacing: 1px;
  }
  .wordmark__name { display: block; font-size: 64px; }
  .wordmark__trade { display: block; font-size: 22px; letter-spacing: 2px; }
  .card--front .wordmark { color: var(--silver); }
  .card--back .wordmark { position: absolute; right: 40px; top: 30px; color: var(--lime); text-align: right; }
  .card--back .wordmark__name { font-size: 54px; }
  .card--back .wordmark__trade { font-size: 18px; }

  .divider {
    position: absolute; left: 36px; right: 36px; top: 160px;
    height: 1px; background: var(--rule);
  }
  .phones {
    position: absolute; right: 40px; top: 180px;
    list-style: none; color: var(--ink); font-size: 15px; text-align: right;
  }
  .phones li { display: flex; align-items: center; justify-content: flex-end; gap: 6px; line-height: 22px; }
  .icon { width: 14px; height: 14px; fill: var(--lime); flex: none; }

  .person { position: absolute; left: 40px; top: 222px; }
  .person__name {
    font-family: "Ubuntu", Arial, sans-serif; font-weight: 700;
    color: var(--lime); font-size: 26px; letter-spacing: 1px;
  }
  .person__role { color: var(--ink); font-size: 14px; margin-top: -2px; }
  .contact { list-style: none; margin-top: 14px; color: var(--ink); font-size: 15px; }
  .contact li { display: flex; align-items: center; gap: 7px; line-height: 22px; }
</style>
</head>
<body>
<main class="stage">

  <section class="card card--front" aria-label="Card front">
    <p class="wordmark">
      <span class="wordmark__name">CORAL</span>
      <span class="wordmark__trade">REFRIGERATION</span>
    </p>
  </section>

  <section class="card card--back" aria-label="Card back">
    <p class="wordmark">
      <span class="wordmark__name">CORAL</span>
      <span class="wordmark__trade">REFRIGERATION</span>
    </p>
    <div class="divider"></div>

    <ul class="phones">
      <li>0893172648
        <svg class="icon" viewBox="0 0 16 16" aria-hidden="true"><path d="M3 2h3l1.5 3.5-2 1.2a8 8 0 0 0 3.8 3.8l1.2-2L14 10v3a1 1 0 0 1-1 1A11 11 0 0 1 2 3a1 1 0 0 1 1-1z"/></svg>
      </li>
      <li>0417258391
        <svg class="icon" viewBox="0 0 16 16" aria-hidden="true"><path d="M3 2h3l1.5 3.5-2 1.2a8 8 0 0 0 3.8 3.8l1.2-2L14 10v3a1 1 0 0 1-1 1A11 11 0 0 1 2 3a1 1 0 0 1 1-1z"/></svg>
      </li>
    </ul>

    <div class="person">
      <h1 class="person__name">GAVIN PELLOW</h1>
      <p class="person__role">Director</p>
      <ul class="contact">
        <li>
          <svg class="icon" viewBox="0 0 16 16" aria-hidden="true"><path d="M1 3h14v10H1z M2 4l6 5 6-5" fill="var(--lime)" stroke="var(--card)" stroke-width="1.2"/></svg>
          gavin@coralrefrigeration.com.au
        </li>
        <li>
          <svg class="icon" viewBox="0 0 16 16" aria-hidden="true"><circle cx="8" cy="8" r="7"/><path d="M1 8h14M8 1c-3 3.5-3 10.5 0 14M8 1c3 3.5 3 10.5 0 14" fill="none" stroke="var(--card)" stroke-width="1"/></svg>
          coralrefrigeration.com.au
        </li>
      </ul>
    </div>
  </section>

</main>
</body>
</html>
```